U.S. based testing, inspection, and certification (TIC) company needs a new PowerPoint template.

We need a new PowerPoint template (deck, slide deck) for our U.S. based company with international capabilities for performing numerous testing, inspection, and certification (TIC) services. Our primary services include calibration, chemical analysis, consulting engineering, environmental simulation, forensic engineering, materials testing, mechanical testing, and nondestructive testing. Industries we serve are aerospace/aviation, automotive, chemical, commercial properties, construction, consumer products, defense, energy storage, healthcare, insurance/legal, life science, manufacturing, oil & gas, power generation, pulp & paper, and telecommunications. https://qorvenlab.com/

Guideline hex colors: #29aae2, #0b1f3b, #fb6805 (use orange more subtly)

The final design should communicate:
1. Trust, Integrity, and Independence
2. Technical Expertise and Accuracy
3. Efficiency and Speed
4. Value-Added Partnership

Our current branding reflects a variety of styles, several of which have been included as attachments for reference in this project. While these examples showcase the direction we have taken in the past, we are not limited to them and remain open to exploring fresh, innovative design that is simple, clean, and with plenty of space to add content for each slide. We welcome creative concepts that build on or reimagine our existing identity to better align with our evolving vision.

```html
<!DOCTYPE html>
<html lang="en">
<head>
<meta charset="utf-8">
<title>Qorven Technical Services – Slide Template</title>
<link href="https://fonts.googleapis.com/css2?family=Crimson+Pro:wght@400;600;700&family=Inter:wght@400;500;600;700&display=swap" rel="stylesheet">
<style>
:root{
  --navy:#0b1f3b;
  --blue:#29aae2;
  --orange:#fb6805;
  --orange-soft:#f7964a;
  --ink:#1d2330;
  --muted:#5b6472;
  --line:#9aa1ab;
  --page:#ffffff;
}
*{box-sizing:border-box;margin:0;padding:0}
html,body{width:1200px;height:729px;overflow:hidden;background:var(--page)}
body{position:relative;font-family:"Inter",sans-serif;color:var(--ink)}
.slide{position:absolute;width:380px;height:213px;background:#fff;box-shadow:0 1px 4px rgba(0,0,0,.35);overflow:hidden}
.slide.dark{background:var(--navy);color:#fff}
.c1{left:17px}.c2{left:413px}.c3{left:809px}
.r1{top:26px}.r2{top:255px}.r3{top:484px}
.abs{position:absolute}
.brand{position:absolute;left:14px;top:11px;font:700 6.5px "Inter",sans-serif;letter-spacing:.8px;color:var(--navy)}
.dark .brand{color:#fff}
.tag{position:absolute;right:20px;top:17px;font-size:4.3px;color:var(--ink)}
.tag.blue{color:var(--blue)}
.title{position:absolute;left:22px;top:40px;font:700 11.5px "Crimson Pro",serif;letter-spacing:.9px;text-transform:uppercase;color:var(--navy)}
.title.sans{font:400 12px "Inter",sans-serif;letter-spacing:-.2px}
.rule{position:absolute;left:22px;height:1px;background:var(--orange)}
.foot{position:absolute;bottom:12px;font-size:3.8px;color:var(--ink)}
.foot.l{left:14px}.foot.r{right:14px;color:var(--blue)}
p,li{font-size:4.6px;line-height:1.45;color:var(--ink)}
.serif{font-family:"Crimson Pro",serif}
.card{position:absolute;border:1px solid #8d939c;background:#fff;padding:6px 5px}
.card h3{font:700 7px "Crimson Pro",serif;letter-spacing:.3px;color:var(--navy);margin:6px 0 3px}
.card p{font-size:4.2px;color:var(--muted);line-height:1.45}
.card svg{width:8px;height:8px;display:block}
.photo{position:absolute}
</style>
</head>
<body>

<!-- Slide 1: cover -->
<section class="slide dark c1 r1">
  <div class="brand">QORVEN</div>
  <div class="abs" style="left:105px;top:63px;width:171px;height:12px;border-radius:6px;background:var(--orange-soft);color:#fff;font-size:5.6px;letter-spacing:.6px;text-align:center;line-height:12px">TESTING, INSPECTION, &amp; CERTIFICATION</div>
  <h1 class="abs serif" style="left:0;width:380px;top:80px;text-align:center;font-size:17px;font-weight:700;letter-spacing:.6px">QORVEN TECHNICAL <span style="color:var(--blue)">SERVICES</span></h1>
  <p class="abs" style="left:0;width:380px;top:112px;text-align:center;color:#d8dde6;font-size:5.6px">Ensuring Safety, Quality, and Operational Excellence with International Reach.<br>Engineered for Reliability and Technical Integrity.</p>
  <div class="abs" style="left:80px;top:135px;width:220px;height:.6px;background:#7b8698"></div>
  <p class="abs" style="left:0;width:380px;top:141px;text-align:center;color:#c7ceda;font-size:4.5px">Your Professional Partner in Overcoming Complex Technical Obstacles</p>
</section>

<!-- Slide 2: who we are -->
<section class="slide dark c2 r1">
  <div class="brand">QORVEN</div>
  <div class="abs" style="left:133px;top:81px;width:114px;height:1px;background:var(--orange)"></div>
  <h2 class="abs serif" style="left:0;width:380px;top:91px;text-align:center;font-size:16px;font-weight:700;letter-spacing:.6px">WHO WE ARE</h2>
  <p class="abs" style="left:0;width:380px;top:122px;text-align:center;color:#d8dde6;font-size:4.8px">A trusted, independent TIC provider performing advanced calibration,<br>chemical, and materials services for mission-critical industries globally.</p>
</section>

<!-- Slide 3: pillars -->
<section class="slide c3 r1">
  <div class="brand">QORVEN</div>
  <div class="tag blue">CORE BRAND PILLARS</div>
  <h2 class="title" style="left:24px;top:44px">Our Pillars of Excellence</h2>
  <div class="rule" style="left:24px;top:63px;width:198px"></div>
  <div class="card" style="left:22px;top:87px;width:98px;height:69px">
    <svg viewBox="0 0 10 10"><path d="M5 1v8M2 9h6M1.5 3h7M1.5 3l-1 3h2zM8.5 3l-1 3h2z" stroke="#29aae2" stroke-width=".9" fill="none"/></svg>
    <h3>Integrity &amp; Trust</h3>
    <p>Upholding absolute independence and objective verification in all scientific analyses, complying with rigorous national and international credentials.</p>
  </div>
  <div class="card" style="left:138px;top:87px;width:98px;height:69px">
    <svg viewBox="0 0 10 10"><path d="M3 1h2v5H3zM2 9h7M4 6v3M6 4a3 3 0 0 1 1 5" stroke="#29aae2" stroke-width=".9" fill="none"/></svg>
    <h3>Technical Accuracy</h3>
    <p>Deploying advanced instrumentation and certified engineers to deliver highly precise calibration and inspection results with flawless data integrity.</p>
  </div>
  <div class="card" style="left:254px;top:87px;width:98px;height:69px">
    <svg viewBox="0 0 10 10"><path d="M6 0L2 6h3l-1 4 4-6H5z" fill="#29aae2"/></svg>
    <h3>Efficiency &amp; Speed</h3>
    <p>Executing tests with optimal turnaround times to minimize client downtime, supported by modern automated workflow and logging frameworks.</p>
  </div>
  <div class="foot l">@2026 Qorven Technical Services</div>
  <div class="foot r">qorvenlab.com</div>
</section>

<!-- Slide 4: aerospace -->
<section class="slide c1 r2">
  <div class="brand">QORVEN</div>
  <h2 class="title" style="left:18px;top:34px">Aerospace Diagnostics</h2>
  <div class="rule" style="left:18px;top:50px;width:136px"></div>
  <h3 class="abs serif" style="left:18px;top:80px;font-size:9px;font-weight:700;color:var(--navy)">Analytical Focus</h3>
  <p class="abs" style="left:18px;top:96px;width:175px">Specialists perform product failure assessments to determine if structural degradation is a result of poor original design, manufacturing defects, or operational stress.</p>
  <p class="abs" style="left:18px;top:119px;width:175px">We ensure compliance with the highest FAA aerospace parameters, protecting complex satellite platforms, engine manifolds, and flight instrumentation.</p>
  <p class="abs" style="left:217px;top:44px;width:140px;font-size:3.6px;color:var(--muted)">Aerospace communication satellite platform orbiting in high-earth orbit representing advanced analytical avionics checks.</p>
  <div class="photo" role="img" aria-label="Communication satellite with solar panels orbiting above Earth" style="left:217px;top:59px;width:134px;height:112px;border:1px solid #9aa1ab;background:linear-gradient(160deg,#1a2a4a 0%,#3b5f93 45%,#8fb4dc 75%,#dfe8f3 100%)"></div>
  <div class="foot l">@2026 Qorven Technical Services</div>
  <div class="foot r">qorvenlab.com</div>
</section>

<!-- Slide 5: industries -->
<section class="slide c2 r2">
  <div class="brand">QORVEN</div>
  <div class="tag">INDUSTRIAL FOOTPRINT</div>
  <h2 class="title" style="left:19px;top:33px;font-size:12.5px">Industries Partnering with QTS</h2>
  <div class="rule" style="left:19px;top:51px;width:266px"></div>
  <div class="card" style="left:19px;top:88px;width:100px;height:70px">
    <svg viewBox="0 0 10 10"><path d="M0 5.5l4-1 1.5-4 1 .2-.5 3.8L9.5 4l.5 1.5-4 .8-.5 3.5-1-.2.2-3.3-4 .5z" fill="#29aae2"/></svg>
    <h3>Aerospace &amp; Defense</h3>
    <p>Nondestructive testing, failure analysis, and environmental simulations for commercial spacecraft, satellites, and defence structures.</p>
  </div>
  <div class="card" style="left:135px;top:88px;width:100px;height:70px">
    <svg viewBox="0 0 10 10"><path d="M1 5l1.5-3h5L9 5v3H1z" fill="#29aae2"/><circle cx="3" cy="6.5" r=".8" fill="#fff"/><circle cx="7" cy="6.5" r=".8" fill="#fff"/></svg>
    <h3>Automotive &amp; Transport</h3>
    <p>Verifying structural safety, analyzing metallurgy properties, and certifying vehicle electronics against road environments.</p>
  </div>
  <div class="card" style="left:253px;top:88px;width:100px;height:70px">
    <svg viewBox="0 0 10 10"><path d="M0 10V3l3 2V3l3 2V1h2v9z" fill="#29aae2"/></svg>
    <h3>Energy &amp; Utilities</h3>
    <p>Monitoring nuclear power lines, oil &amp; gas drilling infrastructure, pipeline integrity, and checking energy storage facilities.</p>
  </div>
  <div class="foot l">Aviation, Chemical, Pulp &amp; Paper, Power Gen, and Telecommunications Services</div>
  <div class="foot r">qorvenlab.com</div>
</section>

<!-- Slide 6: services -->
<section class="slide c3 r2">
  <div class="brand">QORVEN</div>
  <div class="tag">TIC CAPABILITIES OVERVIEW</div>
  <h2 class="title" style="left:18px;top:34px">Primary Technical Services</h2>
  <div class="rule" style="left:18px;top:50px;width:192px"></div>
  <ul class="abs" style="left:28px;top:70px;width:200px;list-style:none">
    <li style="margin-bottom:4px"><b class="serif">Calibration &amp; Metrology:</b> Providing precise diagnostic comparisons for high-spec manufacturing tooling and mechanical instruments.</li>
    <li style="margin-bottom:4px"><b class="serif">Materials &amp; Mechanical Testing:</b> Analyzing physical material limits, tensile strength, fatigue, and structural capabilities.</li>
    <li style="margin-bottom:4px"><b class="serif">Chemical Analysis:</b> Determining elemental structures, contamination sources, and molecular composition of compounds.</li>
    <li style="margin-bottom:4px"><b class="serif">Nondestructive Testing (NDT):</b> Deploying advanced radiographic, ultrasonic, and magnetic particle examinations.</li>
    <li><b class="serif">Forensic &amp; Consulting Engineering:</b> Conducting in-depth failure analysis to reconstruct structural failures, trace material fracture mechanics, and present scientific evidence for corporate or litigation purposes.</li>
  </ul>
  <div class="photo" role="img" aria-label="Universal tensile testing machine with control computer" style="left:237px;top:70px;width:110px;height:113px;background:linear-gradient(90deg,#c9ccd1 0%,#e9ebee 40%,#b8bcc3 60%,#eef0f2 100%)"></div>
  <div class="foot l">ISO 17025 Accredited Laboratory Operations</div>
  <div class="foot r">qorvenlab.com</div>
</section>

<!-- Slide 7: market capabilities -->
<section class="slide c1 r3">
  <div class="brand">QORVEN</div>
  <div class="tag">Value-Added Partnership</div>
  <h2 class="title sans" style="left:20px;top:33px">PROVEN MARKET CAPABILITIES</h2>
  <div class="rule" style="left:20px;top:50px;width:194px"></div>
  <div class="abs" style="left:24px;top:80px;width:146px;height:70px;border-radius:9px;background:var(--navy);text-align:center">
    <div class="serif" style="margin-top:16px;font-size:24px;font-weight:700;color:#3a86c4;line-height:1">10K +</div>
    <div style="margin-top:3px;font-size:4.6px;font-weight:600;letter-spacing:.6px;color:var(--orange)">ACTIVE CLIENTS SERVED</div>
  </div>
  <h3 class="abs serif" style="left:198px;top:72px;font-size:9px;font-weight:700;line-height:1.2;color:var(--navy)">Global Competencies,<br>Client Partnership First</h3>
  <p class="abs" style="left:198px;top:101px;width:170px">QTS has built an expansive capability footprint serving major international corporations across five continents with accurate data and testing support.</p>
  <p class="abs" style="left:198px;top:121px;width:170px">Our network of testing laboratories provides unparalleled customer support, protecting brand reputation, solving structural failures, and verifying technical compliance daily.</p>
  <p class="abs" style="left:198px;top:142px;width:170px;color:var(--orange)">Quality, Reliability, and Safety are not just objectives; they are our foundational rules.</p>
  <div class="foot l">Multi-Laboratory International Operations</div>
  <div class="foot r">qorvenlab.com</div>
</section>

<!-- Slide 8: rope access -->
<section class="slide c2 r3">
  <div class="brand">QORVEN</div>
  <h2 class="title" style="left:19px;top:34px;font-weight:600">Rope Access &amp; Advanced NDT</h2>
  <div class="rule" style="left:19px;top:50px;width:199px"></div>
  <div class="photo" role="img" aria-label="Rope access technician working on an elevated steel structure" style="left:19px;top:76px;width:104px;height:104px;border-radius:50%;border:1.5px solid var(--blue);background:linear-gradient(180deg,#dfe6ec 0%,#a9b7c4 60%,#56616d 100%)"></div>
  <h3 class="abs serif" style="left:137px;top:79px;font-size:7.5px;font-weight:700;color:var(--navy)">Reaching Difficult Elements</h3>
  <p class="abs" style="left:137px;top:92px;width:225px">Our SPRAT-certified rope access technicians deploy specialized nondestructive testing methods directly to difficult areas of structural components, such as tall petrochemical towers, wind turbines, bridges, and nuclear silos.</p>
  <ul class="abs" style="left:137px;top:116px;list-style:none">
    <li style="margin-bottom:3px"><svg width="5" height="5" viewBox="0 0 10 10" style="margin-right:3px"><path d="M1 5l3 3 5-7" stroke="#fb6805" stroke-width="1.8" fill="none"/></svg>Rope Access Testing to securely monitor elevated assets.</li>
    <li style="margin-bottom:3px"><svg width="5" height="5" viewBox="0 0 10 10" style="margin-right:3px"><path d="M1 5l3 3 5-7" stroke="#fb6805" stroke-width="1.8" fill="none"/></svg>Reliability testing to detect fatigue cracks and preemptive failure.</li>
    <li><svg width="5" height="5" viewBox="0 0 10 10" style="margin-right:3px"><path d="M1 5l3 3 5-7" stroke="#fb6805" stroke-width="1.8" fill="none"/></svg>NDT diagnostic certification to secure hidden weld locations.</li>
  </ul>
  <div class="foot l">SPRAT &amp; ASNT Certified NDT Operations</div>
  <div class="foot r">qorvenlab.com</div>
</section>

<!-- Slide 9: closing -->
<section class="slide dark c3 r3">
  <h2 class="abs serif" style="left:0;width:380px;top:56px;text-align:center;font-size:18px;font-weight:400;letter-spacing:1.4px">PARTNER WITH QTS</h2>
  <p class="abs" style="left:0;width:380px;top:86px;text-align:center;color:#fff;font-size:6px;font-weight:500">Let our certified team of engineers, chemists, and NDT technicians secure your<br>asset reliability and performance parameters.</p>
  <div class="abs" style="left:112px;top:124px;width:67px;height:13px;border-radius:2px;background:var(--orange-soft);font-size:5px;line-height:13px;color:var(--navy)">
    <svg width="8" height="8" viewBox="0 0 10 10" style="position:absolute;left:4px;top:2.5px"><circle cx="5" cy="5" r="4" stroke="#fff" fill="none" stroke-width=".9"/><path d="M1 5h8M5 1c-2 2.5-2 5.5 0 8M5 1c2 2.5 2 5.5 0 8" stroke="#fff" fill="none" stroke-width=".7"/></svg>
    <span style="position:absolute;left:17px;text-decoration:underline;color:#1d3e8a">www.qorvenlab.com</span>
  </div>
  <div class="abs" style="left:196px;top:124px;width:67px;height:13px;border-radius:2px;background:var(--orange-soft);font-size:5px;line-height:13px;color:#fff">
    <svg width="8" height="8" viewBox="0 0 10 10" style="position:absolute;left:4px;top:2.5px"><circle cx="5" cy="5" r="4.4" stroke="#fff" fill="none" stroke-width=".7"/><path d="M3.3 2.6l1 1.2-.6.7a4 4 0 0 0 1.8 1.8l.7-.6 1.2 1-.6.8C5 7.3 2.7 5 2.5 3.2z" fill="#fff"/></svg>
    <span style="position:absolute;left:20px">1-800-555-0142</span>
  </div>
  <p class="abs" style="left:0;width:380px;top:159px;text-align:center;color:#c7ceda;font-size:3.8px">U.S. Headquartered Company with Advanced International Testing Capabilities</p>
</section>

</body>
</html>
```